Bday & 7th year in Singapore

I'll be celebrating my thirty something birthday and 7th year in Singapore on Sat 29 June 2013, 830pm til late. Still looking for a venue so please leave some space for it and the address so it can be added.
Required:
Sat, 29 June
830pm
Venue TBC
I would like the poster to have an "infographic" look and feel, ideally with blue, grey, and red tones.
I would like invitees to feel that it's going to a great night of live music, drinks and mingling with existing and new friends so it would be awesome if they can be there.
I love traveling, clubbing, going on food adventures, singing.
People need to know that it's primarily a bday party (main design element) but that I'm also celebrating my 7th year in Singapore.
I'm looking for the most creative design so people will get excited and book their diaries as soon as they see the invitation.
Output required: high quality JPEG I can post on Pindlebox event page and also something I can use for A3 printing. Winning designer should be able to accommodate a revision on venue after decision is made as I can only confirm venue after the deadline.
Reason: Extended the deadline as I realise 2 days is quite tight given nature of the project.
Reason: Waiting for venue to be confirmed so it can be built into the poster
Target Market(s)
Invitees would be between 23 and 35 years old so should appeal to them
Industry/Entity Type
Printing
Requirements
Must have
- Singapore famous landmarks like Corlow Quay Towers, Singapore skyline, Verandine, Tidecrest, but they should not be the centre of attraction
Nice to have
- My photo (attached) but drawn in a nice way

```html
<!DOCTYPE html>
<html lang="en">
<head>
<meta charset="utf-8">
<title>Theo's Birthday and 7th Year in Singapore</title>
<link rel="stylesheet" href="https://fonts.googleapis.com/css2?family=Anton&family=Oswald:wght@300;400;500;600&display=swap">
<style>
  :root {
    --ink: #000000;
    --sky-light: #d6ecf7;
    --sky: #8cc7e4;
    --sky-deep: #4f9fc9;
    --band: #8fc3dc;
    --band-text: #0e2230;
    --tagline: #a9d8ee;
    --white: #ffffff;
    --red: #e23a3f;
    --night-1: #0b1622;
    --night-2: #1e3345;
    --night-3: #5a5440;
    --shirt-red: #d9473c;
    --flag-white: #f1eeea;
    --skin: #c9a08a;
  }
  html, body {
    margin: 0;
    padding: 0;
    width: 853px;
    height: 1200px;
    overflow: hidden;
    background: var(--ink);
  }
  .poster {
    position: relative;
    width: 853px;
    height: 1200px;
    background: var(--ink);
    overflow: hidden;
    font-family: "Oswald", "Arial Narrow", sans-serif;
  }
  .skyline-photo {
    position: absolute;
    left: 204px;
    top: 342px;
    width: 649px;
    height: 500px;
    background:
      radial-gradient(ellipse at 68% 72%, rgba(230, 210, 160, 0.45) 0%, rgba(230, 210, 160, 0) 40%),
      linear-gradient(180deg, var(--ink) 0%, var(--night-1) 25%, var(--night-2) 60%, var(--night-3) 85%, var(--ink) 100%);
    -webkit-mask-image: linear-gradient(90deg, transparent 0%, #000 18%, #000 100%);
    mask-image: linear-gradient(90deg, transparent 0%, #000 18%, #000 100%);
  }
  .title {
    position: absolute;
    left: 0;
    width: 853px;
    margin: 0;
    text-align: center;
    font-family: "Anton", "Impact", sans-serif;
    font-weight: 400;
    text-transform: uppercase;
    line-height: 1;
    background: linear-gradient(180deg, var(--sky-light) 0%, var(--sky) 55%, var(--sky-deep) 100%);
    -webkit-background-clip: text;
    background-clip: text;
    color: transparent;
  }
  .title-name {
    top: 22px;
    font-size: 172px;
    letter-spacing: -2px;
  }
  .title-event {
    top: 168px;
    font-size: 200px;
    letter-spacing: -3px;
  }
  .subtitle {
    position: absolute;
    top: 374px;
    left: 0;
    width: 853px;
    margin: 0;
    text-align: center;
    color: var(--white);
    font-weight: 500;
    font-size: 34px;
    letter-spacing: 1px;
    text-transform: uppercase;
  }
  .tagline {
    position: absolute;
    top: 446px;
    left: 0;
    width: 853px;
    margin: 0;
    text-align: center;
    color: var(--tagline);
    font-weight: 500;
    text-transform: uppercase;
    line-height: 1.18;
  }
  .tagline-main {
    display: block;
    font-size: 25px;
    letter-spacing: 0.5px;
  }
  .tagline-aside {
    display: block;
    font-size: 20px;
    font-weight: 400;
    letter-spacing: 0.5px;
  }
  .guest-photo {
    position: absolute;
    left: 24px;
    top: 540px;
    width: 456px;
    height: 660px;
    background:
      radial-gradient(ellipse 28% 20% at 42% 22%, var(--skin) 0%, rgba(201, 160, 138, 0) 100%),
      linear-gradient(160deg, var(--shirt-red) 30%, var(--flag-white) 60%, #bfb9b3 100%);
    border-radius: 46% 46% 0 0 / 26% 26% 0 0;
    -webkit-mask-image: linear-gradient(90deg, #000 75%, transparent 100%);
    mask-image: linear-gradient(90deg, #000 75%, transparent 100%);
  }
  .details {
    position: absolute;
    left: 484px;
    top: 800px;
    width: 310px;
    text-align: center;
    color: var(--white);
  }
  .details p { margin: 0; }
  .date {
    color: var(--red);
    font-weight: 500;
    font-size: 72px;
    line-height: 1;
    text-transform: uppercase;
  }
  .day {
    color: var(--red);
    font-weight: 300;
    font-size: 72px;
    line-height: 1;
    text-transform: uppercase;
    margin-top: 2px !important;
  }
  .time {
    font-weight: 500;
    font-size: 34px;
    line-height: 1;
    margin-top: 12px !important;
    text-transform: uppercase;
  }
  .venue {
    font-weight: 300;
    font-size: 18px;
    line-height: 1.65;
    margin-top: 26px !important;
    text-transform: uppercase;
  }
  .phone {
    font-weight: 400;
    font-size: 24px;
    line-height: 1.2;
  }
  .phone strong { font-weight: 500; }
  .footer-band {
    position: absolute;
    left: 0;
    top: 1110px;
    width: 853px;
    height: 31px;
    background: var(--band);
  }
  .footer-cta {
    position: absolute;
    left: 484px;
    top: 1110px;
    width: 310px;
    height: 31px;
    margin: 0;
    text-align: center;
    line-height: 31px;
    color: var(--band-text);
    font-weight: 500;
    font-size: 17px;
    text-transform: uppercase;
  }
</style>
</head>
<body>
  <main class="poster">
    <div class="skyline-photo" role="img" aria-label="Night photograph of the Singapore skyline with Corlow Quay Towers, the Verandine and the Tidecrest statue spouting water"></div>

    <h1>
      <span class="title title-name">Theo’s</span>
      <span class="title title-event">Birthday</span>
    </h1>

    <p class="subtitle">And 7th year in Singapore</p>

    <p class="tagline">
      <span class="tagline-main">Great night of live music,</span>
      <span class="tagline-main">food &amp; drinks with friends</span>
      <span class="tagline-aside">(and potentially new ones!)</span>
    </p>

    <div class="footer-band"></div>

    <div class="guest-photo" role="img" aria-label="Photograph of the birthday host in glasses and a red striped shirt, waving a Singapore flag"></div>

    <section class="details">
      <p class="date">June 29th</p>
      <p class="day">Saturday</p>
      <p class="time">Starts at 8:30pm</p>
      <p class="venue">Harlow Hotel • 1729 Bellmont Ave<br>Ridgefield, NJ 07214-318</p>
      <p class="phone">Tel.: <strong>(555) 018-2047</strong></p>
    </section>

    <p class="footer-cta">Be awesome! Be there!</p>
  </main>
</body>
</html>
```